Business Card for my Photography/Video Business

I would like the card to say Event Photographer and Videographer. I like the Black and Gold look to it as well but open to other options. I don't want it to be super vibrant or colorful. Simple, elegant and professional

```html
<!DOCTYPE html>
<html lang="en">
<head>
<meta charset="utf-8">
<title>Northlight – Business Card</title>
<link rel="stylesheet" href="https://fonts.googleapis.com/css2?family=Josefin+Sans:wght@300;400&family=Kaushan+Script&display=swap">
<style>
  :root {
    --backdrop: #1b1b1b;
    --card: #232323;
    --card-edge: #2c2c2c;
    --mark: #0e0e0e;
    --brand-text: #d9d9d9;
    --gold: #d9b23c;
    --ink-light: #ececec;
    --rule: #bdbdbd;
  }
  * { margin: 0; padding: 0; box-sizing: border-box; }
  html, body {
    width: 1200px;
    height: 900px;
    overflow: hidden;
    background: var(--backdrop);
  }
  .canvas {
    position: relative;
    width: 1200px;
    height: 900px;
    display: flex;
    flex-direction: column;
    align-items: center;
    justify-content: center;
    gap: 50px;
  }
  .card {
    position: relative;
    width: 588px;
    height: 336px;
    background: var(--card);
    border: 1px solid var(--card-edge);
    border-radius: 6px;
    box-shadow: 0 14px 30px rgba(0,0,0,0.55);
    overflow: hidden;
  }

  /* Front: brand */
  .card--brand {
    display: flex;
    align-items: center;
    justify-content: center;
    padding: 0 48px;
    gap: 16px;
  }
  .brand-dot {
    width: 96px;
    height: 96px;
    border-radius: 50%;
    background: var(--mark);
    flex: none;
  }
  .brand-name {
    font-family: "Josefin Sans", sans-serif;
    font-weight: 400;
    font-size: 46px;
    letter-spacing: 3px;
    color: var(--brand-text);
    text-transform: uppercase;
    line-height: 1;
    padding-top: 6px;
    white-space: nowrap;
  }

  /* Back: person */
  .card--person {
    display: flex;
    flex-direction: column;
    align-items: center;
    justify-content: center;
  }
  .divider {
    position: relative;
    width: 420px;
    height: 20px;
    display: flex;
    align-items: center;
    justify-content: center;
  }
  .divider::before {
    content: "";
    position: absolute;
    left: 0; right: 0; top: 50%;
    border-top: 1px solid var(--rule);
  }
  .divider__ornament {
    position: relative;
    width: 64px;
    height: 8px;
    border-radius: 4px;
    background: var(--rule);
    opacity: 0.75;
  }
  .person-name {
    font-family: "Kaushan Script", cursive;
    font-weight: 400;
    font-size: 64px;
    color: var(--gold);
    line-height: 1.1;
    margin-top: 22px;
    white-space: nowrap;
  }
  .person-role {
    font-family: "Josefin Sans", sans-serif;
    font-weight: 300;
    font-size: 17px;
    letter-spacing: 2px;
    color: var(--ink-light);
    text-transform: uppercase;
    margin: 8px 0 24px;
    white-space: nowrap;
  }
</style>
</head>
<body>
  <main class="canvas">
    <section class="card card--brand">
      <span class="brand-dot"></span>
      <span class="brand-name">Northlight</span>
    </section>

    <section class="card card--person">
      <div class="divider">
        <span class="divider__ornament" role="img" aria-label="small decorative flourish"></span>
      </div>
      <h1 class="person-name">Leo Hartwell</h1>
      <p class="person-role">Event Photographer &amp; Videographer</p>
      <div class="divider">
        <span class="divider__ornament" role="img" aria-label="small decorative flourish"></span>
      </div>
    </section>
  </main>
</body>
</html>
```